Poster Design Project

About Us
Lumvik is a company that specializes in providing communication solutions to the travel market. Our simple vision of “every hotel should have a mobile phone in the guest rooms”, led us to develop a path breaking cost effective mobile phone. With full integration capabilities with the hotels property management system, location based marketing, user locator and other features, this product is unique in addressing the hospitality segment.
Product Placement
The Lumvik mobile will be placed in the hotel room on an A4 Sized transparent stand (the transparent stand is attached for your reference. If you notice, the phone will be placed in the jacket on the bottom left and in another jacket on the bottom right will be the brochure. So effectively, the design space available on the A4 brochure is only 60% of the space). The designed poster that we wish designed will be inserted in the A4 sized acrylic stand. The stand would typically be on the bedside table or on the study table of the hotel room. The A4 design should be bright and vibrant in keeping with our logo colors.
Attached is our logo. Also attached is the symbol of our phone that could be used innovatively on the brochure if you think it helps.
Attached is the content for the poster.
Reason: Feedback from the management team got delayed, hence the extension. Thanks
Reason: The delay is in the content finalization.

```html
<!DOCTYPE html>
<html lang="en">
<head>
<meta charset="utf-8">
<title>Lumvik – Keep Talking Poster</title>
<link rel="stylesheet" href="https://fonts.googleapis.com/css2?family=Arimo:wght@400;700&display=swap">
<style>
  :root {
    --orange: #f7982f;
    --orange-deep: #e07d10;
    --ink: #111111;
    --paper: #ffffff;
  }
  * { margin: 0; padding: 0; box-sizing: border-box; }
  html, body { width: 848px; height: 1200px; overflow: hidden; background: var(--paper); }
  .poster {
    position: relative;
    width: 848px;
    height: 1200px;
    background: var(--paper);
    font-family: "Arimo", Arial, sans-serif;
    color: var(--ink);
    overflow: hidden;
  }
  .brand-mark {
    position: absolute;
    left: 25px;
    top: 25px;
    width: 218px;
    height: 218px;
    border-radius: 50%;
    background: var(--orange);
  }
  .brand-name {
    position: absolute;
    left: 290px;
    top: 20px;
    font-size: 150px;
    font-weight: 400;
    line-height: 1;
    color: var(--orange);
    letter-spacing: 4px;
  }
  .tagline {
    position: absolute;
    left: 374px;
    top: 168px;
    font-size: 22px;
    letter-spacing: 1.5px;
  }
  .benefits {
    position: absolute;
    left: 282px;
    top: 212px;
    list-style: none;
  }
  .benefits li {
    display: flex;
    align-items: center;
    height: 46.5px;
    font-size: 23px;
    font-weight: 700;
    letter-spacing: 1px;
  }
  .benefits li::before {
    content: "";
    width: 18px;
    height: 18px;
    margin-right: 15px;
    border-radius: 50%;
    background: radial-gradient(circle at 50% 40%, var(--orange) 55%, var(--orange-deep) 70%, #3a2410 100%);
    flex: none;
  }
  .brochure-note {
    position: absolute;
    left: 27px;
    top: 452px;
    font-size: 15px;
    line-height: 21px;
  }
  .call-to-action {
    position: absolute;
    left: 488px;
    top: 420px;
    width: 340px;
    height: 264px;
  }
  .cta-text {
    position: absolute;
    left: 540px;
    width: 236px;
    text-align: center;
    font-weight: 700;
  }
  .cta-lead { top: 435px; font-size: 24px; letter-spacing: 0.5px; }
  .cta-now {
    top: 472px;
    font-size: 62px;
    font-weight: 400;
    letter-spacing: 6px;
    color: var(--orange);
    -webkit-text-stroke: 1.5px var(--ink);
  }
  .cta-tail { top: 571px; font-size: 22px; }
  .service-notes {
    position: absolute;
    left: 27px;
    top: 1096px;
    list-style: none;
    font-size: 13px;
    line-height: 20px;
  }
</style>
</head>
<body>
<main class="poster">
  <div class="brand-mark" aria-hidden="true"></div>
  <h1 class="brand-name">Lumvik</h1>
  <p class="tagline">Lumvik Keep Talking</p>

  <ul class="benefits">
    <li>SAVE 80% on international roaming</li>
    <li>Get a LOCAL number</li>
    <li>60 FREE minutes of international calls</li>
    <li>60 FREE minutes of local calls</li>
    <li>499 BHT</li>
  </ul>

  <p class="brochure-note">Refer to the brochure<br>for more details</p>

  <svg class="call-to-action" viewBox="488 420 340 264" aria-hidden="true">
    <rect x="540" y="421" width="235" height="164" fill="var(--orange)"/>
    <rect x="489" y="584" width="336" height="11" fill="var(--orange)"/>
    <polygon points="530,608 784,608 770,625 545,625" fill="var(--orange)"/>
    <polygon points="569,632 745,632 727,651 590,651" fill="var(--orange)"/>
    <polygon points="594,654 707,654 651,681" fill="var(--orange)"/>
  </svg>
  <p class="cta-text cta-lead">Pick up this phone</p>
  <p class="cta-text cta-now">NOW</p>
  <p class="cta-text cta-tail">to keep talking...</p>

  <ul class="service-notes">
    <li>Itemized bill on checkout</li>
    <li>Flexible tariff plans to choose from</li>
    <li>Excellent call quality</li>
  </ul>
</main>
</body>
</html>
```